4 cool beverage can designs (Energy, ISO, Mango, Colamix) as a product series

About us
Brinvale Motorsport is an international off-road motorsport team from Switzerland, specialised in the Rally Quorvenne and Quorvenne Heritage. We are producing four drink flavours as printed cans, used as team and event drinks. We are looking for a strong, consistent design in the style of well-known energy brands (think Vortag Fuel): bold, vibrant and instantly recognisable.
The task
Design four can designs (250ml SlimLine) that work together as a clearly recognisable series (same design language, same base layout, same logo placement), while each flavour is clearly distinct from the others. Important: the flavour should be recognisable at first glance, ideally through one clear base colour per flavour.
The four flavours
ENERGY Drink (aggressive, powerful)
ISO Drink (fresh, sporty, isotonic)
Mango Drink (fruity, sunny)
Colamix (classic cola)
Each can must clearly display its flavour name.
Colours (idea only, not fixed)
The colour choice is entirely up to you as the designer. The only requirement is that each flavour gets its own clearly distinguishable colour world and that the flavour is intuitively recognisable. As non-binding inspiration: Energy could be red, ISO blue, Mango orange, Colamix black. Feel free to surprise us with your own bold ideas, as long as the four flavours stay easy to tell apart.
Style and look
Cool, modern, high energy, premium feel in the style of Vortag Fuel, Kestrix, Zonda
Vibrant, punchy colours are explicitly encouraged
Dynamic graphic elements welcome (splashes, claw marks, light streaks, abstract shapes, carbon, energy effects)
A reference to motorsport, rally or desert is allowed but not required (e.g. tyre tracks, speed, off-road). Use it only if it makes the design stronger
The four cans must clearly read as one family when placed side by side
Must include
The Brinvale Motorsport logo, clearly visible and prominently placed (logo file will be provided)
The flavour name, clearly legible (ENERGY, ISO, MANGO, COLAMIX)
Consistent logo position and design system across all four cans
No-gos
The official Quorvenne logo as well as official Quorvenne wordmarks and trademarks must NOT be used for legal reasons (a general motorsport or desert look is fine, just no protected Quorvenne branding)
No pale or pastel colours
No cluttered or overloaded layouts where the logo and flavour name get lost
No designs that only work for a single flavour and do not fit the series
No designs that cannot be technically implemented in the pelvaro.de configurator (see technical specs). Submissions that do not work there will not be considered
Technical specifications (mandatory, production runs via pelvaro.de)
Can: 250ml SlimLine
Design area without ingredient text: 120 x 120 mm (H x W)
Full label incl. ingredients/mandatory info: 170 x 120 mm (H x W)
Resolution: 300 dpi
Colour mode: CMYK (4/0 or 5/0 print)
Keep space free for the deposit label (50 x 25 mm); this area must not be covered by important design elements
Please work exactly within the official pelvaro.de layout template (available at pelvaro.de/de/layoutvorlagen). Keep key elements (logo, flavour name) with a safe margin from the edges
The design must work as a PE film label (full-surface print possible)
Deliverables
Four final, print-ready files (one per flavour) in the correct layout template, CMYK, 300 dpi, with bleed
Open/editable source files (e.g. Adobe Illustrator AI or Photoshop PSD), fonts embedded or converted to outlines
Optional but appreciated: a 3D mockup preview per can
Judging criteria
Instant recognisability of the flavour
Visibility and impact of the Brinvale Motorsport logo
Coolness and recognition in the style of strong energy brands
Consistency as one unified set of four
Technical feasibility in the pelvaro.de configurator
Layout Template https://www.pelvaro.de/en/layoutvorlagen

```html
<!DOCTYPE html>
<html lang="de">
<head>
<meta charset="utf-8">
<title>Brinvale Motorsport – Can Series</title>
<link rel="stylesheet" href="https://fonts.googleapis.com/css2?family=Alfa+Slab+One&family=Anton&family=Arimo:wght@400;700&family=Montserrat:wght@600;700&family=Oswald:wght@700&family=Yellowtail&display=swap">
<style>
  :root {
    --ink: #0a0a0a;
    --band: #1b1b1b;
    --white: #ffffff;
    --paper: #ffffff;
    --iso: #1c6fd0; --iso-hi: #2f8cf0; --iso-deep: #0c3366; --iso-dark: #050d18;
    --mango: #df6410; --mango-hi: #f5821f; --mango-deep: #5a2607; --mango-dark: #120903;
    --energy: #c40f0f; --energy-hi: #e01a1a; --energy-deep: #4d0505; --energy-dark: #120202;
    --cola: #7d5c33; --cola-hi: #927045; --cola-deep: #3a2713; --cola-dark: #0e0905;
  }
  * { box-sizing: border-box; margin: 0; padding: 0; }
  html, body { width: 872px; height: 1200px; overflow: hidden; background: var(--paper); }
  body { position: relative; font-family: "Arimo", Arial, sans-serif; color: var(--white); }

  .flavour-iso    { --c: var(--iso);    --hi: var(--iso-hi);    --deep: var(--iso-deep);    --dark: var(--iso-dark); }
  .flavour-mango  { --c: var(--mango);  --hi: var(--mango-hi);  --deep: var(--mango-deep);  --dark: var(--mango-dark); }
  .flavour-energy { --c: var(--energy); --hi: var(--energy-hi); --deep: var(--energy-deep); --dark: var(--energy-dark); }
  .flavour-cola   { --c: var(--cola);   --hi: var(--cola-hi);   --deep: var(--cola-deep);   --dark: var(--cola-dark); }

  /* ---------- flat label ---------- */
  .label {
    position: absolute; width: 384px; height: 272px; overflow: hidden;
    background: linear-gradient(90deg, var(--dark) 0%, var(--deep) 22%, var(--c) 40%, var(--hi) 50%, var(--ink) 56%, var(--ink) 70%, var(--c) 80%, var(--deep) 92%, var(--dark) 100%);
  }
  .vert { position: absolute; writing-mode: vertical-rl; transform: rotate(180deg); white-space: nowrap; }

  .info { position: absolute; left: 20px; top: 10px; width: 104px; font-size: 3.5px; line-height: 4.4px; }
  .info__type { font-weight: 400; font-size: 8px; line-height: 10px; margin-bottom: 2px; }
  .info p { margin-bottom: 3px; text-align: justify; }
  .nutri { width: 100%; border: 0.6px solid var(--white); padding: 2px 3px; margin: 3px 0 4px; border-collapse: separate; font-size: 3.4px; line-height: 4.2px; }
  .nutri th { text-align: left; font-weight: 700; }
  .nutri td:last-child { text-align: right; }
  .nutri .note { text-align: left !important; }
  .info__maker { line-height: 4.3px; }

  .marks { position: absolute; left: 20px; top: 224px; display: flex; gap: 4px; }
  .marks span { width: 12px; height: 12px; border-radius: 50%; border: 1.2px solid var(--white); }
  .made { position: absolute; left: 20px; top: 240px; font-size: 4px; }
  .content { position: absolute; left: 20px; top: 246px; font-size: 9px; line-height: 9px; }
  .powered { position: absolute; left: 80px; top: 238px; width: 46px; text-align: center; font-family: "Montserrat", sans-serif; font-weight: 700; font-size: 3.4px; letter-spacing: 0.6px; line-height: 4px; }
  .powered i { display: block; width: 9px; height: 9px; margin: 0 auto 2px; border-radius: 50%; background: var(--white); }

  .splash { position: absolute; left: 196px; top: 0; width: 98px; height: 100%;
    background: linear-gradient(90deg, transparent 0%, rgba(0,0,0,.85) 14%, #000 30%, #000 75%, rgba(0,0,0,.85) 88%, transparent 100%); }
  .tread { position: absolute; left: 214px; top: 0; width: 46px; height: 100%; background: var(--band); }

  .flavour-name { color: var(--white); }
  .flavour-name--iso    { font-family: "Anton", sans-serif; font-size: 64px; line-height: 64px; left: 150px; bottom: -30px; letter-spacing: 2px; }
  .flavour-name--mango  { font-family: "Alfa Slab One", serif; font-size: 46px; line-height: 50px; left: 146px; bottom: 70px; }
  .flavour-name--energy { font-family: "Anton", sans-serif; font-size: 58px; line-height: 60px; left: 148px; bottom: 60px; }
  .flavour-name--cola   { font-family: "Yellowtail", cursive; font-size: 62px; line-height: 60px; left: 140px; bottom: 56px; }

  .flavour-tag { left: 193px; bottom: 92px; font-family: "Montserrat", sans-serif; font-weight: 600; font-size: 6px; letter-spacing: 2.4px; line-height: 8px; }

  .brand { font-family: "Oswald", sans-serif; font-weight: 700; color: var(--white); text-transform: uppercase; }
  .brand span { display: block; }
  .label .brand { left: 218px; bottom: 46px; }
  .label .brand .brand__main { font-size: 34px; line-height: 34px; }
  .label .brand .brand__sub { font-size: 13.5px; line-height: 14px; letter-spacing: 2.6px; }

  .claim { font-family: "Montserrat", sans-serif; font-weight: 700; letter-spacing: 1.6px; color: var(--white); }
  .claim b { color: var(--c); }
  .label .claim { left: 368px; bottom: 12px; font-size: 8px; line-height: 10px; }

  /* ---------- flat can panels ---------- */
  .panel { position: absolute; width: 84px; height: 224px; overflow: hidden; }
  .panel--info  { background: linear-gradient(90deg, var(--dark) 0%, var(--deep) 55%, var(--c) 100%); }
  .panel--front { background: linear-gradient(90deg, var(--c) 0%, var(--hi) 45%, var(--ink) 58%, var(--band) 80%, var(--band) 100%); }
  .panel--back  { background: linear-gradient(90deg, var(--ink) 0%, var(--band) 20%, var(--band) 48%, var(--c) 66%, var(--deep) 88%, var(--dark) 100%); }

  .panel .info { left: 6px; top: 6px; width: 66px; font-size: 2.8px; line-height: 3.5px; }
  .panel .info__type { font-size: 6px; line-height: 7px; }
  .panel .nutri { font-size: 2.6px; line-height: 3.2px; }
  .panel .content { left: 6px; top: 198px; font-size: 7px; line-height: 7px; }
  .panel .made { left: 6px; top: 192px; font-size: 3px; }
  .panel .powered { left: 40px; top: 196px; width: 38px; font-size: 2.6px; line-height: 3.2px; }
  .panel .powered i { width: 7px; height: 7px; }

  .panel .flavour-name--iso    { font-size: 52px; line-height: 54px; left: 4px; bottom: -20px; }
  .panel .flavour-name--mango  { font-size: 36px; line-height: 40px; left: 6px; bottom: 40px; }
  .panel .flavour-name--energy { font-size: 46px; line-height: 48px; left: 4px; bottom: 36px; }
  .panel .flavour-name--cola   { font-size: 48px; line-height: 48px; left: 2px; bottom: 36px; }
  .panel .flavour-tag { left: 48px; bottom: 60px; font-size: 4.2px; line-height: 6px; letter-spacing: 1.8px; }
  .panel--front .brand { left: 56px; bottom: 26px; }
  .panel--back .brand  { left: 10px; bottom: 26px; }
  .panel .brand .brand__main { font-size: 24px; line-height: 24px; }
  .panel .brand .brand__sub { font-size: 9.5px; line-height: 10px; letter-spacing: 1.8px; }
  .panel .claim { left: 72px; bottom: 8px; font-size: 5.6px; line-height: 7px; letter-spacing: 1.1px; }
</style>
</head>
<body>

<!-- ===================== ISO label ===================== -->
<section class="label flavour-iso" style="left:22px; top:12px;">
  <div class="splash" role="img" aria-label="Black paint splatter texture"></div>
  <div class="tread" role="img" aria-label="Tyre track band"></div>
  <div class="info">
    <h2 class="info__type">ISO-Drink</h2>
    <p><b>Isotonisches Erfrischungsgetränk Grapefruit-Zitronengeschmack mit Zucker und Süßungsmitteln. 6 Vitamine zugesetzt.</b></p>
    <p><b>Zutaten:</b> Wasser, Fruktosesirup, 2,5% Orangensaft aus Orangensaftkonzentrat, 2% Grapefruitsaft aus Grapefruitsaftkonzentrat, 1,5% Zitronensaft aus Zitronensaftkonzentrat, Kohlensäure, Zitronenextrakt, Säuerungsmittel: Citronensäure, Säureregulator: Kaliumcitrate, Magnesiumcarbonate; Süßungsmittel: Cyclamat, Saccharin; natürliches Citrusaroma, Vitaminmischung: Vitamin C, Niacin, Vitamin E, Pantothensäure, Folsäure, Biotin; Stabilisator: Johannisbrotkernmehl, Antioxidationsmittel: Ascorbinsäure. Mindestens haltbar bis: siehe Boden. Kühl und trocken lagern.</p>
    <table class="nutri">
      <tr><th colspan="2">Durchschnittliche Nährwerte je 100ml</th></tr>
      <tr><td>Brennwert</td><td>79 kJ (19 kcal)</td></tr>
      <tr><td>Fett</td><td>0 g</td></tr>
      <tr><td>- davon gesättigte Fettsäuren</td><td>0 g</td></tr>
      <tr><td>Kohlenhydrate</td><td>4,3 g</td></tr>
      <tr><td>- davon Zucker</td><td>4,3 g</td></tr>
      <tr><td>Eiweiß</td><td>0,1 g</td></tr>
      <tr><td>Salz</td><td>0,06 g</td></tr>
      <tr><td>Vitamin C</td><td>14,4 mg / 18%*</td></tr>
      <tr><td>Niacin</td><td>2,9 mg / 18%*</td></tr>
      <tr><td>Vitamin E</td><td>2,16 mg / 18%*</td></tr>
      <tr><td>Pantothensäure</td><td>1,08 mg / 18%*</td></tr>
      <tr><td>Folsäure</td><td>36,0 µg / 18%*</td></tr>
      <tr><td>Biotin</td><td>9,0 µg / 18%*</td></tr>
      <tr><td class="note" colspan="2">*NRV = Referenzmenge für die tägliche Zufuhr</td></tr>
    </table>
    <p class="info__maker"><b>Hersteller:</b><br>Halverin GmbH<br>Lindenhofer Str. 12<br>93180 Falkenried<br><b>www.pelvaro.de</b><br><b>Vertrieb:</b><br>Musterfirma GmbH<br>Musterstraße 1<br>00000 Musterstadt</p>
  </div>
  <div class="marks"><span></span><span></span></div>
  <div class="made">MADE IN GERMANY</div>
  <div class="content">Inhalt<br>250ml ℮</div>
  <div class="powered"><i></i>POWERED BY<br>BRINVALE MOTORSPORT</div>
  <div class="vert flavour-name flavour-name--iso">ISO ISO ISO</div>
  <div class="vert flavour-tag">DRINK FLAVOUR</div>
  <div class="vert brand"><span class="brand__main">Brinvale</span><span class="brand__sub">Motorsport</span></div>
  <div class="vert claim">PASSION <b>•</b> PRECISION <b>•</b> PERFORMANCE</div>
</section>

<!-- ===================== MANGO label ===================== -->
<section class="label flavour-mango" style="left:470px; top:12px;">
  <div class="splash" role="img" aria-label="Black paint splatter texture"></div>
  <div class="tread" role="img" aria-label="Tyre track band"></div>
  <div class="info">
    <h2 class="info__type">ISO-Drink</h2>
    <p><b>Isotonisches Erfrischungsgetränk Grapefruit-Zitronengeschmack mit Zucker und Süßungsmitteln. 6 Vitamine zugesetzt.</b></p>
    <p><b>Zutaten:</b> Wasser, Fruktosesirup, 2,5% Orangensaft aus Orangensaftkonzentrat, 2% Grapefruitsaft aus Grapefruitsaftkonzentrat, 1,5% Zitronensaft aus Zitronensaftkonzentrat, Kohlensäure, Zitronenextrakt, Säuerungsmittel: Citronensäure, Säureregulator: Kaliumcitrate, Magnesiumcarbonate; Süßungsmittel: Cyclamat, Saccharin; natürliches Citrusaroma, Vitaminmischung: Vitamin C, Niacin, Vitamin E, Pantothensäure, Folsäure, Biotin; Stabilisator: Johannisbrotkernmehl, Antioxidationsmittel: Ascorbinsäure. Mindestens haltbar bis: siehe Boden. Kühl und trocken lagern.</p>
    <table class="nutri">
      <tr><th colspan="2">Durchschnittliche Nährwerte je 100ml</th></tr>
      <tr><td>Brennwert</td><td>79 kJ (19 kcal)</td></tr>
      <tr><td>Fett</td><td>0 g</td></tr>
      <tr><td>- davon gesättigte Fettsäuren</td><td>0 g</td></tr>
      <tr><td>Kohlenhydrate</td><td>4,3 g</td></tr>
      <tr><td>- davon Zucker</td><td>4,3 g</td></tr>
      <tr><td>Eiweiß</td><td>0,1 g</td></tr>
      <tr><td>Salz</td><td>0,06 g</td></tr>
      <tr><td>Vitamin C</td><td>14,4 mg / 18%*</td></tr>
      <tr><td>Niacin</td><td>2,9 mg / 18%*</td></tr>
      <tr><td>Vitamin E</td><td>2,16 mg / 18%*</td></tr>
      <tr><td>Pantothensäure</td><td>1,08 mg / 18%*</td></tr>
      <tr><td>Folsäure</td><td>36,0 µg / 18%*</td></tr>
      <tr><td>Biotin</td><td>9,0 µg / 18%*</td></tr>
      <tr><td class="note" colspan="2">*NRV = Referenzmenge für die tägliche Zufuhr</td></tr>
    </table>
    <p class="info__maker"><b>Hersteller:</b><br>Halverin GmbH<br>Lindenhofer Str. 12<br>93180 Falkenried<br><b>www.pelvaro.de</b><br><b>Vertrieb:</b><br>Musterfirma GmbH<br>Musterstraße 1<br>00000 Musterstadt</p>
  </div>
  <div class="marks"><span></span><span></span></div>
  <div class="made">MADE IN GERMANY</div>
  <div class="content">Inhalt<br>250ml ℮</div>
  <div class="powered"><i></i>POWERED BY<br>BRINVALE MOTORSPORT</div>
  <div class="vert flavour-name flavour-name--mango">Mango</div>
  <div class="vert flavour-tag">DRINK FLAVOUR</div>
  <div class="vert brand"><span class="brand__main">Brinvale</span><span class="brand__sub">Motorsport</span></div>
  <div class="vert claim">PASSION <b>•</b> PRECISION <b>•</b> PERFORMANCE</div>
</section>

<!-- ===================== ENERGY label ===================== -->
<section class="label flavour-energy" style="left:22px; top:308px;">
  <div class="splash" role="img" aria-label="Black paint splatter texture"></div>
  <div class="tread" role="img" aria-label="Tyre track band"></div>
  <div class="info">
    <h2 class="info__type">ENERGY DRINK</h2>
    <p><b>Koffeinhaltiges Erfrischungsgetränk mit Zusatz von 4 Vitaminen. Erhöhter Koffeingehalt (30 mg/100 ml). Für Kinder, schwangere oder stillende Frauen nicht empfohlen.</b></p>
    <p><b>Zutaten:</b> Wasser, Zucker, Dextrose, Säuerungsmittel Citronensäure, Kohlensäure, Säureregulator Natriumcitrate, Koffein, Taurin (0,03%), Farbstoffe E150c und E101, Inosit, Aroma, Niacin, Pantothensäure, Vitamin B6, Vitamin B12.</p>
    <p>Mindestens haltbar bis Ende: siehe Dosenboden. Kühl und trocken lagern.</p>
    <table class="nutri">
      <tr><th colspan="2">Durchschnittliche Nährwerte je 100ml</th></tr>
      <tr><td>Brennwert</td><td>195 kJ(45,9 kcal)</td></tr>
      <tr><td>Fett</td><td>0 g</td></tr>
      <tr><td>- davon gesättigte Fettsäuren</td><td>0 g</td></tr>
      <tr><td>Kohlenhydrate</td><td>10,9 g</td></tr>
      <tr><td>- davon Zucker</td><td>10,9 g</td></tr>
      <tr><td>Eiweiß</td><td>0,06 g</td></tr>
      <tr><td>Salz</td><td>0,273 g</td></tr>
      <tr><th colspan="2">Vitamine</th></tr>
      <tr><td>Niacin</td><td>7,92 mg/49,5%*</td></tr>
      <tr><td>Pantothensäure</td><td>1,98 mg/33,0%*</td></tr>
      <tr><td>Vitamin B6</td><td>2 mg/143,0%*</td></tr>
      <tr><td>Vitamin B12</td><td>2 µg/80,0%*</td></tr>
      <tr><td class="note" colspan="2">*NRV = Referenzmenge für die tägliche Zufuhr</td></tr>
    </table>
    <p class="info__maker"><b>Hersteller:</b><br>Halverin GmbH<br>Lindenhofer Str. 12<br>93180 Falkenried<br><b>www.pelvaro.de</b><br><br>Musterfirma GmbH<br>Musterstraße 1<br>00000 Musterstadt</p>
  </div>
  <div class="marks"><span></span><span></span></div>
  <div class="made">MADE IN GERMANY</div>
  <div class="content">Inhalt<br>250ml ℮</div>
  <div class="powered"><i></i>POWERED BY<br>BRINVALE MOTORSPORT</div>
  <div class="vert flavour-name flavour-name--energy">ENERGY</div>
  <div class="vert flavour-tag">DRINK FLAVOUR</div>
  <div class="vert brand"><span class="brand__main">Brinvale</span><span class="brand__sub">Motorsport</span></div>
  <div class="vert claim">PASSION <b>•</b> PRECISION <b>•</b> PERFORMANCE</div>
</section>

<!-- ===================== COLAMIX label ===================== -->
<section class="label flavour-cola" style="left:470px; top:308px;">
  <div class="splash" role="img" aria-label="Black paint splatter texture"></div>
  <div class="tread" role="img" aria-label="Tyre track band"></div>
  <div class="info">
    <h2 class="info__type">ENERGY DRINK</h2>
    <p><b>Koffeinhaltiges Erfrischungsgetränk mit Zusatz von 4 Vitaminen. Erhöhter Koffeingehalt (30 mg/100 ml). Für Kinder, schwangere oder stillende Frauen nicht empfohlen.</b></p>
    <p><b>Zutaten:</b> Wasser, Zucker, Dextrose, Säuerungsmittel Citronensäure, Kohlensäure, Säureregulator Natriumcitrate, Koffein, Taurin (0,03%), Farbstoffe E150c und E101, Inosit, Aroma, Niacin, Pantothensäure, Vitamin B6, Vitamin B12.</p>
    <p>Mindestens haltbar bis Ende: siehe Dosenboden. Kühl und trocken lagern.</p>
    <table class="nutri">
      <tr><th colspan="2">Durchschnittliche Nährwerte je 100ml</th></tr>
      <tr><td>Brennwert</td><td>195 kJ(45,9 kcal)</td></tr>
      <tr><td>Fett</td><td>0 g</td></tr>
      <tr><td>- davon gesättigte Fettsäuren</td><td>0 g</td></tr>
      <tr><td>Kohlenhydrate</td><td>10,9 g</td></tr>
      <tr><td>- davon Zucker</td><td>10,9 g</td></tr>
      <tr><td>Eiweiß</td><td>0,06 g</td></tr>
      <tr><td>Salz</td><td>0,273 g</td></tr>
      <tr><th colspan="2">Vitamine</th></tr>
      <tr><td>Niacin</td><td>7,92 mg/49,5%*</td></tr>
      <tr><td>Pantothensäure</td><td>1,98 mg/33,0%*</td></tr>
      <tr><td>Vitamin B6</td><td>2 mg/143,0%*</td></tr>
      <tr><td>Vitamin B12</td><td>2 µg/80,0%*</td></tr>
      <tr><td class="note" colspan="2">*NRV = Referenzmenge für die tägliche Zufuhr</td></tr>
    </table>
    <p class="info__maker"><b>Hersteller:</b><br>Halverin GmbH<br>Lindenhofer Str. 12<br>93180 Falkenried<br><b>www.pelvaro.de</b><br><br>Musterfirma GmbH<br>Musterstraße 1<br>00000 Musterstadt</p>
  </div>
  <div class="marks"><span></span><span></span></div>
  <div class="made">MADE IN GERMANY</div>
  <div class="content">Inhalt<br>250ml ℮</div>
  <div class="powered"><i></i>POWERED BY<br>BRINVALE MOTORSPORT</div>
  <div class="vert flavour-name flavour-name--cola">Colamix</div>
  <div class="vert flavour-tag">DRINK FLAVOUR</div>
  <div class="vert brand"><span class="brand__main">Brinvale</span><span class="brand__sub">Motorsport</span></div>
  <div class="vert claim">PASSION <b>•</b> PRECISION <b>•</b> PERFORMANCE</div>
</section>

<!-- ===================== Can views: ISO ===================== -->
<div class="panel panel--info flavour-iso" style="left:82px; top:652px;">
  <div class="info">
    <h2 class="info__type">ISO-Drink</h2>
    <p><b>Isotonisches Erfrischungsgetränk Grapefruit-Zitronengeschmack mit Zucker und Süßungsmitteln.</b></p>
    <p><b>Zutaten:</b> Wasser, Fruktosesirup, Orangensaft, Grapefruitsaft, Zitronensaft, Kohlensäure, Citronensäure, Kaliumcitrate, Cyclamat, Saccharin, Citrusaroma, Vitamine.</p>
    <table class="nutri">
      <tr><th colspan="2">Nährwerte je 100ml</th></tr>
      <tr><td>Brennwert</td><td>79 kJ (19 kcal)</td></tr>
      <tr><td>Kohlenhydrate</td><td>4,3 g</td></tr>
      <tr><td>Eiweiß</td><td>0,1 g</td></tr>
      <tr><td>Salz</td><td>0,06 g</td></tr>
    </table>
    <p class="info__maker"><b>Hersteller:</b> Halverin GmbH<br>www.pelvaro.de</p>
  </div>
  <div class="made">MADE IN GERMANY</div>
  <div class="content">Inhalt<br>250ml ℮</div>
  <div class="powered"><i></i>POWERED BY<br>BRINVALE MOTORSPORT</div>
</div>
<div class="panel panel--front flavour-iso" style="left:187px; top:652px;">
  <div class="vert flavour-name flavour-name--iso">ISO ISO</div>
  <div class="vert flavour-tag">DRINK FLAVOUR</div>
  <div class="vert brand"><span class="brand__main">Brinvale</span><span class="brand__sub">Motorsport</span></div>
</div>
<div class="panel panel--back flavour-iso" style="left:308px; top:652px;">
  <div class="vert brand"><span class="brand__main">Brinvale</span><span class="brand__sub">Motorsport</span></div>
  <div class="vert claim">PASSION <b>•</b> PRECISION <b>•</b> PERFORMANCE</div>
</div>

<!-- ===================== Can views: MANGO ===================== -->
<div class="panel panel--info flavour-mango" style="left:487px; top:652px;">
  <div class="info">
    <h2 class="info__type">ISO-Drink</h2>
    <p><b>Isotonisches Erfrischungsgetränk Grapefruit-Zitronengeschmack mit Zucker und Süßungsmitteln.</b></p>
    <p><b>Zutaten:</b> Wasser, Fruktosesirup, Orangensaft, Grapefruitsaft, Zitronensaft, Kohlensäure, Citronensäure, Kaliumcitrate, Cyclamat, Saccharin, Citrusaroma, Vitamine.</p>
    <table class="nutri">
      <tr><th colspan="2">Nährwerte je 100ml</th></tr>
      <tr><td>Brennwert</td><td>79 kJ (19 kcal)</td></tr>
      <tr><td>Kohlenhydrate</td><td>4,3 g</td></tr>
      <tr><td>Eiweiß</td><td>0,1 g</td></tr>
      <tr><td>Salz</td><td>0,06 g</td></tr>
    </table>
    <p class="info__maker"><b>Hersteller:</b> Halverin GmbH<br>www.pelvaro.de</p>
  </div>
  <div class="made">MADE IN GERMANY</div>
  <div class="content">Inhalt<br>250ml ℮</div>
  <div class="powered"><i></i>POWERED BY<br>BRINVALE MOTORSPORT</div>
</div>
<div class="panel panel--front flavour-mango" style="left:597px; top:652px;">
  <div class="vert flavour-name flavour-name--mango">Mango</div>
  <div class="vert flavour-tag">DRINK FLAVOUR</div>
  <div class="vert brand"><span class="brand__main">Brinvale</span><span class="brand__sub">Motorsport</span></div>
</div>
<div class="panel panel--back flavour-mango" style="left:714px; top:652px;">
  <div class="vert brand"><span class="brand__main">Brinvale</span><span class="brand__sub">Motorsport</span></div>
  <div class="vert claim">PASSION <b>•</b> PRECISION <b>•</b> PERFORMANCE</div>
</div>

<!-- ===================== Can views: COLAMIX ===================== -->
<div class="panel panel--info flavour-cola" style="left:82px; top:924px;">
  <div class="info">
    <h2 class="info__type">ENERGY DRINK</h2>
    <p><b>Koffeinhaltiges Erfrischungsgetränk mit Zusatz von 4 Vitaminen. Erhöhter Koffeingehalt.</b></p>
    <p><b>Zutaten:</b> Wasser, Zucker, Dextrose, Citronensäure, Kohlensäure, Natriumcitrate, Koffein, Taurin, Farbstoffe, Inosit, Aroma, Vitamine.</p>
    <table class="nutri">
      <tr><th colspan="2">Nährwerte je 100ml</th></tr>
      <tr><td>Brennwert</td><td>195 kJ(45,9 kcal)</td></tr>
      <tr><td>Kohlenhydrate</td><td>10,9 g</td></tr>
      <tr><td>Eiweiß</td><td>0,06 g</td></tr>
      <tr><td>Salz</td><td>0,273 g</td></tr>
    </table>
    <p class="info__maker"><b>Hersteller:</b> Halverin GmbH<br>www.pelvaro.de</p>
  </div>
  <div class="made">MADE IN GERMANY</div>
  <div class="content">Inhalt<br>250ml ℮</div>
  <div class="powered"><i></i>POWERED BY<br>BRINVALE MOTORSPORT</div>
</div>
<div class="panel panel--front flavour-cola" style="left:187px; top:924px;">
  <div class="vert flavour-name flavour-name--cola">Colamix</div>
  <div class="vert flavour-tag">DRINK FLAVOUR</div>
  <div class="vert brand"><span class="brand__main">Brinvale</span><span class="brand__sub">Motorsport</span></div>
</div>
<div class="panel panel--back flavour-cola" style="left:308px; top:924px;">
  <div class="vert brand"><span class="brand__main">Brinvale</span><span class="brand__sub">Motorsport</span></div>
  <div class="vert claim">PASSION <b>•</b> PRECISION <b>•</b> PERFORMANCE</div>
</div>

<!-- ===================== Can views: ENERGY ===================== -->
<div class="panel panel--info flavour-energy" style="left:487px; top:924px;">
  <div class="info">
    <h2 class="info__type">ENERGY DRINK</h2>
    <p><b>Koffeinhaltiges Erfrischungsgetränk mit Zusatz von 4 Vitaminen. Erhöhter Koffeingehalt.</b></p>
    <p><b>Zutaten:</b> Wasser, Zucker, Dextrose, Citronensäure, Kohlensäure, Natriumcitrate, Koffein, Taurin, Farbstoffe, Inosit, Aroma, Vitamine.</p>
    <table class="nutri">
      <tr><th colspan="2">Nährwerte je 100ml</th></tr>
      <tr><td>Brennwert</td><td>195 kJ(45,9 kcal)</td></tr>
      <tr><td>Kohlenhydrate</td><td>10,9 g</td></tr>
      <tr><td>Eiweiß</td><td>0,06 g</td></tr>
      <tr><td>Salz</td><td>0,273 g</td></tr>
    </table>
    <p class="info__maker"><b>Hersteller:</b> Halverin GmbH<br>www.pelvaro.de</p>
  </div>
  <div class="made">MADE IN GERMANY</div>
  <div class="content">Inhalt<br>250ml ℮</div>
  <div class="powered"><i></i>POWERED BY<br>BRINVALE MOTORSPORT</div>
</div>
<div class="panel panel--front flavour-energy" style="left:597px; top:924px;">
  <div class="vert flavour-name flavour-name--energy">ENERGY</div>
  <div class="vert flavour-tag">DRINK FLAVOUR</div>
  <div class="vert brand"><span class="brand__main">Brinvale</span><span class="brand__sub">Motorsport</span></div>
</div>
<div class="panel panel--back flavour-energy" style="left:714px; top:924px;">
  <div class="vert brand"><span class="brand__main">Brinvale</span><span class="brand__sub">Motorsport</span></div>
  <div class="vert claim">PASSION <b>•</b> PRECISION <b>•</b> PERFORMANCE</div>
</div>

</body>
</html>
```